Chiropractic Flyers to be made more up to date

I have used this series of flyers for my own practice. I would like the graphics to be brought up to date and the name of the doctor and the practice, the address, phone number and date to be removed and a blank box inserted in one place on the flyer that other chiropractors could use to personalize the flyers for their practice. On some of the flyers, this information is in several places. I'd like to have it all in one space so that it would be easy for the doctor to add it in their practice. They all need to be bright and colorful with catchy graphics.

Industry/Entity Type

Doctor

```html
<!DOCTYPE html>
<html lang="en">
<head>
<meta charset="utf-8">
<title>Chiropractic Flyers</title>
<link rel="stylesheet" href="https://fonts.googleapis.com/css2?family=Cinzel:wght@400;600&family=Roboto+Condensed:ital,wght@0,400;0,700;1,400&display=swap">
<style>
  :root {
    --backdrop: #5d5f63;
    --holiday-green: #2d7629;
    --holiday-glow: #52c23e;
    --plum: #5c3957;
    --plum-glow: #7b4f72;
    --paper: #f4f4f4;
    --paper-shade: #d9d9d9;
    --ink: #2e2e2e;
    --white: #ffffff;
  }
  * { margin: 0; padding: 0; box-sizing: border-box; }
  html, body { width: 1200px; height: 1000px; overflow: hidden; }
  body { background: var(--backdrop); position: relative; font-family: "Roboto Condensed", Arial, sans-serif; }

  .flyer {
    position: absolute; top: 110px; width: 547px; height: 772px;
    box-shadow: 0 4px 14px rgba(0,0,0,.45);
    overflow: hidden;
  }
  .flyer--charity { left: 38px; }
  .flyer--backpack { left: 617px; }

  .flyer__panel { position: absolute; left: 0; top: 0; width: 100%; height: 608px; color: var(--white); text-align: center; }
  .flyer--charity .flyer__panel { background: radial-gradient(ellipse 280px 220px at 50% 300px, var(--holiday-glow), var(--holiday-green) 100%); }
  .flyer--backpack .flyer__panel { background: radial-gradient(ellipse 300px 260px at 55% 290px, var(--plum-glow), var(--plum) 100%); }

  .notch { position: absolute; left: 256px; top: 607px; width: 36px; height: 19px; z-index: 2; }

  .headline { font-family: "Cinzel", "Times New Roman", serif; font-weight: 600; line-height: 1; position: absolute; left: 0; width: 100%; }
  .headline--kicker { top: 40px; font-size: 34px; }
  .headline--line { font-size: 58px; }
  .headline--line-1 { top: 84px; }
  .headline--line-2 { top: 136px; }
  .headline--main { top: 45px; font-size: 52px; }
  .headline--sub { top: 88px; font-size: 29px; }

  .artwork { position: absolute; }
  .artwork--gifts { left: 105px; top: 190px; width: 340px; height: 245px; background: linear-gradient(160deg, #c9332c 0%, #b32020 45%, #3aa33a 75%, #c7a55a 100%); border-radius: 4px; opacity: .9; }
  .artwork--backpack { left: 188px; top: 178px; width: 160px; height: 260px; background: linear-gradient(180deg, #b27fa6 0%, #8e5a84 50%, #5a3a55 100%); border-radius: 40px 40px 20px 20px; }

  .offer { position: absolute; left: 0; top: 463px; width: 100%; }
  .offer__title { font-weight: 700; font-size: 18px; margin-bottom: 4px; }
  .offer__body { font-size: 13px; line-height: 17px; }
  .offer__body small { font-size: 9px; font-style: italic; }
  .offer__invite { font-size: 12px; line-height: 16px; font-style: italic; margin-top: 16px; }
  .offer__note { font-size: 7px; font-style: italic; margin-top: 14px; }

  .tagline { position: absolute; left: 0; top: 486px; width: 100%; font-family: "Cinzel", "Times New Roman", serif; font-size: 31px; font-weight: 600; }
  .lesson-list { position: absolute; left: 0; top: 533px; width: 100%; list-style: none; font-size: 12.5px; line-height: 15px; }

  .flyer__footer { position: absolute; left: 0; top: 608px; width: 100%; height: 164px; background: linear-gradient(180deg, var(--white) 0%, var(--paper) 60%, var(--paper-shade) 100%); text-align: center; color: var(--ink); }
  .doctor-name { font-family: "Cinzel", "Times New Roman", serif; font-size: 46px; font-weight: 400; line-height: 1; margin-top: 34px; }
  .doctor-address { font-family: "Cinzel", "Times New Roman", serif; font-size: 13px; margin-top: 2px; }
  .doctor-contact { font-family: "Cinzel", "Times New Roman", serif; font-size: 12px; margin-top: 17px; }
  .doctor-contact .divider { margin: 0 6px; }
</style>
</head>
<body>

<section class="flyer flyer--charity">
  <div class="flyer__panel">
    <h1 class="headline headline--kicker">Help Us Help the</h1>
    <p class="headline headline--line headline--line-1">Less Fortunate</p>
    <p class="headline headline--line headline--line-2">Children</p>
    <div class="artwork artwork--gifts" role="img" aria-label="Pile of wrapped holiday gift boxes in red, green and gold with bows"></div>
    <div class="offer">
      <p class="offer__title">In exchange for a Toys or Children’s Books:</p>
      <p class="offer__body">All exams will be given at no charge.&nbsp; All X-rays will be given at no charge. <small>(Taken only if necessary)</small><br>All scoliosis screenings will be given at no charge and Free refreshments!</p>
      <p class="offer__invite">This would be a good opportunity to introduce a friend or member of your family to chiropractic care.<br>You may also take advantage of this offer yourself!!!</p>
      <p class="offer__note">*Offer not valid for Medicare, worker’s comp. or personal injury cases.</p>
    </div>
  </div>
  <svg class="notch" viewBox="0 0 36 19" aria-hidden="true"><polygon points="0,0 36,0 18,19" fill="var(--holiday-green)"/></svg>
  <footer class="flyer__footer">
    <p class="doctor-name">Doctor’s Name</p>
    <p class="doctor-address">Address, City, State</p>
    <p class="doctor-contact">Telephone (555) 123-4567<span class="divider">|</span>Email Name@Domain.com</p>
  </footer>
</section>

<section class="flyer flyer--backpack">
  <div class="flyer__panel">
    <h1 class="headline headline--main">Backpack Safety</h1>
    <p class="headline headline--sub">Demonstration</p>
    <div class="artwork artwork--backpack" role="img" aria-label="Purple school backpack filled with notebooks and a water bottle"></div>
    <p class="tagline">Stand up for Success!</p>
    <ul class="lesson-list">
      <li>Learn how your posture can effect your attitude &amp; self-esteem.</li>
      <li>Learn the posture of a “Winner” &amp; how to avoid the posture of a “Loser”.</li>
      <li>Learn proper backpack safety to stand up for success.</li>
    </ul>
  </div>
  <svg class="notch" viewBox="0 0 36 19" aria-hidden="true"><polygon points="0,0 36,0 18,19" fill="var(--plum)"/></svg>
  <footer class="flyer__footer">
    <p class="doctor-name">Doctor’s Name</p>
    <p class="doctor-address">Address, City, State</p>
    <p class="doctor-contact">Telephone (555) 123-4567<span class="divider">|</span>Email Name@Domain.com</p>
  </footer>
</section>

</body>
</html>
```